Implant and Mini Implant trifold brochure.

Logo is attached. Our website: www.q7rdental.com

We need an Implant and Mini Implant Flyer (on the same flyer) to be done by someone experienced in Dental marketing.

To be mailed via : Each Block Bulk Post-Counter® (EBBP Counter®)
You need to put a Retail Indica
Reference: https://www.natpostal.example/business/each-block-bulk-post.htm
Each Block Bulk Post-Counter Indicia Guidelines

Every EBBP mailpiece must have an EBBP indicia with “ECRWSS” in the address area, within the permit indicia, or below the permit, like the examples to the right.
The EBBP Counter Indicia does not have a specific size requirement but must be larger than .5" x .5".
The type font must be in all caps and at least a 4 point size.
Place the indicia in the upper right hand corner of the mailpiece.
It should fit in the area 1.625" from the right edge and 1.375" from top edge.
Leave 1/8" of space around the top and right edge.

There should be a picture of a senior citizen eating apple - that is what implants will provide.

One side English; Other side Spanish.

If you do not have idea on what implants and mini-implants are then please ask specific questions.

Make space for specials.

Target Market(s)

dental implants, dental mini implants

Font styles to use
Other font styles liked:
• leaving it open for designer.

Colors
00a990
33b8a4
87cfc6
cadf82

Requirements
Must have
• A senior citizen eating apple - that is what implants allow people to do.
• Once the design layout is finalized, we will provide text. I am leaving the design wide open. you may look at good templates for ideas, but please respect the copyright.
Nice to have
• Use implant and mini implant pictures.
• Images needed
• 1) 3 Easy Steps to Implant Restoration in 1 visit: Use three images: mouth with missing teeth; mouth with implant screws fitted; mouth with teeth restored.
• 2) Image for Implant based Denture.
• 3) Senior Citizen or a couple eating apple.
• Image must be of good quality; even if taken from different sources they must gel well with the over all design. The final design has to be stunning.
• Please do not provide me with designs that I can get from any printing company.
• The Text area:
• 1. Why Implants?
• 2. Space for implant based dentures.
• 3. Other spaces for filling in "Why visit q7r Dental"
• Additional Info: Time to use the following text in the final output.
• q7r Dental - Your base for Crown-to-Root Dental care.
• q7r Dental - Your Implant Harbor.
• Why Implants?
• . Durable, long lasting teeth replacement
• . Surgically implanted metal posts or frames into the jawbone
• . Allows crowns, bridges or complete dentures to be placed on implants
• Why Implant Dentures?
• . Durable and Cost Effective
• . Your denture fabricated as normal denture
• . Four or more implants are placed in one visit
• . Your denture is then retrofitted to snap on the mini implant retention head
• . Stabilize your loose dentures in one visit
• Why Mini Implants?
• . Less involved procedure than conventional implants
• . Usually completed in one dental appointment
• . Replace missing teeth instantly
• Implants vs Mini-Implants
• Visit q7r Dental for a complementary consultation to learn which option is best for you. Depending on various conditions including that of the jawbone, you may be recommended an implant or mini-implant based treatment.
• Implant or Mini-implant treatment may not be suitable for all patients. For implants to be successful, you need to have healthy gums and adequate bones to support the implants. You must also be willing to commit to proper maintenance of your implants or dentures. Visit your dentist at q7r Dental to learn more.
• Spanish translation from google added below:
• q7r Dental: su base para atención Corona-a-Raíz dental.
• q7r Dental: su puerto de implante.
• ¿Por qué los implantes?
• . Reemplazo duradero y duradero de los dientes
• . Puestos o marcos de metal implantados quirúrgicamente en la mandíbula
• . Permiten para colocan coronas, puentes o dentaduras completas en implantes
• ¿Por qué las dentaduras postizas?
• . Durable y rentable
• . Su dentadura fabricada como dentadura normal
• . Cuatro o más implantes se colocan en una visita
• . Su dentadura se reajusta para encajar en el cabezal de retención mini implante
• . Estabilice sus dentaduras sueltas en una visita
• ¿Por qué Mini Implantes?
• . Procedimiento menos complicado que los implantes convencionales
• . Generalmente se completa en una cita dental
• . Reemplace los dientes perdidos al
• Implantes vs Mini Implantes
• Visite q7r Dental para obtener una consulta complementaria y conocer cuál es la mejor opción para usted. Dependiendo de varias condiciones, incluida de la mandíbula, se le puede recomenda un tratamiento basado en implantes o mini-implantes.
• El tratamiento con implantes o mini-implantes puede no ser adecuado para todos los pacientes. Para que los implantes tengan éxito, debe tener encías sanas y huesos adecuados para apoyar los implantes. También debe estar dispuesto a comprometerse con el mantenimiento adecuado de sus implantes o dentaduras postizas. Visite a su dentista en q7r Dental para obtener más información.
Should not have
• blank spaces without purpose

```html
<!DOCTYPE html>
<html lang="en">
<head>
<meta charset="utf-8">
<title>q7r Dental – Implant &amp; Mini Implant Trifold</title>
<link rel="stylesheet" href="https://fonts.googleapis.com/css2?family=Ubuntu:wght@400;500;700&family=Kaushan+Script&display=swap">
<style>
:root{
  --blue:#1460a8;
  --blue-dark:#0c4a8a;
  --green:#8dc63f;
  --lime:#cddc39;
  --lime-head:#d2df3a;
  --ink:#2b2b2b;
  --grey-text:#4a4a4a;
  --paper:#ffffff;
  --backdrop:#c8c9ca;
  --sans:"Ubuntu",Arial,sans-serif;
  --script:"Kaushan Script",cursive;
}
*{box-sizing:border-box;margin:0;padding:0}
html,body{width:1200px;height:1199px;overflow:hidden}
body{background:var(--backdrop);font-family:var(--sans);position:relative}
.spread{position:absolute;left:240px;width:720px;height:556px;background:var(--paper);overflow:hidden;box-shadow:0 4px 10px rgba(0,0,0,.35)}
.spread--outside{top:28px}
.spread--inside{top:614px}
.spread-art{position:absolute;inset:0;width:720px;height:556px}
.abs{position:absolute}
.head{font-weight:700;line-height:1.05;text-transform:uppercase}
.head--lime{color:var(--lime-head)}
.head--blue{color:var(--blue)}
.head--green{color:var(--green)}
.script{font-family:var(--script);line-height:1.1}
.photo-circle{position:absolute;border-radius:50%;border:3px solid var(--green);background:radial-gradient(circle at 50% 40%,#f3d7c6,#c99a86 70%,#a77a67)}
.photo-circle--smile{background:radial-gradient(circle at 50% 55%,#f6efe8,#e2b59d 60%,#cf9a80)}
.photo-circle--couple{background:linear-gradient(150deg,#e9d2bd,#c3a28c 55%,#8ea36a)}

.ticks{list-style:none;position:absolute}
.ticks li{display:flex;align-items:center;gap:10px}
.ticks svg{flex:0 0 auto}

/* practice name (set as plain text) */
.brand{position:absolute;font-family:var(--sans);font-weight:700;color:var(--blue);white-space:nowrap;line-height:1}

.indicia{position:absolute;border:1px solid #222;background:#fff}
.indicia-text{position:absolute;left:50%;top:50%;transform:translate(-50%,-50%) rotate(-90deg);font-family:Arial,sans-serif;color:#111;white-space:nowrap;text-align:left;line-height:1.15}

.url-pill{position:absolute;height:20px;border-radius:10px;color:#fff;font-size:9.5px;letter-spacing:1.6px;display:flex;align-items:center;justify-content:center;font-weight:500}
.url-pill--blue{background:var(--blue)}
.url-pill--green{background:linear-gradient(90deg,var(--lime),var(--green));color:var(--blue-dark)}

.step{position:absolute;left:18px;width:220px;height:66px}
.step .photo-circle{left:6px;top:0;width:64px;height:64px}
.step-num{position:absolute;left:0;top:2px;width:22px;height:22px;border-radius:50%;background:var(--blue);color:#fff;font-weight:700;font-size:15px;display:flex;align-items:center;justify-content:center;border:2px solid #fff}
.step-title{position:absolute;left:78px;top:0;font-size:9px;font-weight:500;color:var(--green);width:130px;line-height:1.2}
.step-body{position:absolute;left:78px;top:13px;font-size:7px;color:var(--ink);width:118px;line-height:1.3}

.photo-caption{color:#fff;text-shadow:0 1px 3px rgba(0,0,0,.55)}
</style>
</head>
<body>

<section class="spread spread--outside" aria-label="Brochure outside">
  <svg class="spread-art" viewBox="0 0 720 556">
    <defs>
      <linearGradient id="blueBand" x1="0" y1="0" x2="1" y2="1">
        <stop offset="0" stop-color="#1460a8"/><stop offset="1" stop-color="#0c4a8a"/>
      </linearGradient>
      <linearGradient id="softGreen" x1="0" y1="0" x2="1" y2="1">
        <stop offset="0" stop-color="#f6f7e6"/><stop offset=".6" stop-color="#e6efc2"/><stop offset="1" stop-color="#a9cf57"/>
      </linearGradient>
      <linearGradient id="seniorPhoto" x1="0" y1="0" x2="0" y2="1">
        <stop offset="0" stop-color="#b8d46a"/><stop offset=".35" stop-color="#d9a07a"/><stop offset=".7" stop-color="#b77858"/><stop offset="1" stop-color="#e8e0cf"/>
      </linearGradient>
      <linearGradient id="skyWhite" x1="0" y1="0" x2="0" y2="1">
        <stop offset="0" stop-color="#ffffff"/><stop offset="1" stop-color="#eef4f9"/>
      </linearGradient>
    </defs>
    <path d="M0 0H240V160C190 200 110 150 0 192Z" fill="url(#blueBand)"/>
    <path d="M0 192C110 150 190 200 240 160V178C190 222 110 172 0 214Z" fill="#8dc63f"/>
    <rect x="480" y="0" width="240" height="260" fill="url(#skyWhite)"/>
    <path d="M240 215C310 222 405 248 441 298C458 272 470 260 480 252V556H240Z" fill="url(#softGreen)"/>
    <path role="img" aria-label="Photo of a smiling senior woman with glasses biting a green apple" d="M480 252C560 212 660 196 720 144V556H480Z" fill="url(#seniorPhoto)"/>
    <path d="M240 204C320 212 410 240 441 286C456 262 470 250 480 244C560 200 660 182 720 132" stroke="#cddc39" stroke-width="6" fill="none"/>
    <path d="M240 214C320 222 410 250 441 296C456 272 470 260 480 252C560 210 660 192 720 142" stroke="#1460a8" stroke-width="8" fill="none"/>
    <line x1="240" y1="0" x2="240" y2="556" stroke="#e3e3e3" stroke-width="1"/>
  </svg>

  <!-- Panel A -->
  <h2 class="abs head head--lime" style="left:25px;top:27px;font-size:19px">Why Implants?</h2>
  <ul class="ticks" style="left:28px;top:58px;width:190px;color:#fff;font-size:9px;line-height:1.3">
    <li style="height:34px"><svg width="20" height="20" viewBox="0 0 20 20"><path d="M2 9h4v9H2zM7 9l4-7c2 0 2 2 1.5 4H17c1.5 0 2 1 1.6 2.2l-2 7.5c-.3 1-1 1.3-2 1.3H7z" fill="#fff"/></svg><span>Durable, long lasting teeth<br>replacement</span></li>
    <li style="height:38px"><svg width="20" height="22" viewBox="0 0 20 22"><circle cx="6" cy="4" r="2.6" fill="none" stroke="#fff" stroke-width="1.6"/><path d="M6 7v13" stroke="#fff" stroke-width="2"/><path d="M14 2v18" stroke="#fff" stroke-width="2"/><path d="M12 3h4" stroke="#fff" stroke-width="2"/></svg><span>Surgically implanted metal posts or<br>frames into the jawbone</span></li>
    <li style="height:38px"><svg width="20" height="24" viewBox="0 0 20 24"><path d="M3 3c3-2 5 0 7 0s4-2 7 0c2 2 1 6-1 8h-12c-2-2-3-6-1-8z" fill="#fff"/><path d="M7 13h6M7 16h6M8 19h4" stroke="#fff" stroke-width="1.6"/></svg><span>Allows crowns, bridges or complete<br>dentures to be placed on implants</span></li>
  </ul>
  <div class="photo-circle photo-circle--couple" role="img" aria-label="Photo of a smiling senior couple" style="left:20px;top:171px;width:76px;height:76px"></div>
  <div class="photo-circle photo-circle--smile" role="img" aria-label="Close-up photo of a bright smile" style="left:89px;top:178px;width:68px;height:68px"></div>

  <h2 class="abs head head--blue" style="left:25px;top:263px;font-size:17px">3 Easy Steps to</h2>
  <h2 class="abs head head--green" style="left:25px;top:283px;font-size:16.5px">Implant Restoration</h2>
  <h3 class="abs head head--blue" style="left:25px;top:304px;font-size:12.5px">In 1 Visit:</h3>

  <div class="step" style="top:329px">
    <div class="photo-circle photo-circle--smile" role="img" aria-label="Photo of a mouth with missing teeth"></div>
    <div class="step-num">1</div>
    <p class="step-title">Mouth with missing teeth</p>
    <p class="step-body">Lorem ipsum dolor sit amet, consectetuer adipiscing elit, sed diam nonummy nibh euismod tincidunt ut laoreet dolore magna</p>
  </div>
  <div class="step" style="top:399px">
    <div class="photo-circle photo-circle--smile" role="img" aria-label="Photo of a mouth with implant screws fitted"></div>
    <div class="step-num">2</div>
    <p class="step-title">Mouth with implant screws fitted</p>
    <p class="step-body" style="top:24px">Lorem ipsum dolor sit amet, consectetuer adipiscing elit, sed diam nonummy nibh euismod tincidunt ut laoreet dolore magna</p>
  </div>
  <div class="step" style="top:472px">
    <div class="photo-circle photo-circle--smile" role="img" aria-label="Photo of a mouth with teeth restored"></div>
    <div class="step-num">3</div>
    <p class="step-title">Mouth with teeth restored</p>
    <p class="step-body">Lorem ipsum dolor sit amet, consectetuer adipiscing elit, sed diam nonummy nibh euismod tincidunt ut laoreet dolore magna</p>
  </div>

  <!-- Panel B -->
  <div class="indicia" style="left:263px;top:19px;width:61px;height:81px">
    <p class="indicia-text" style="font-size:8px">PRSRT STD<br>ECRWSS<br>U.S.POSTAGE<br><b style="font-size:9.5px">PAID</b><br>EBBP Counter</p>
  </div>
  <div class="indicia" style="left:381px;top:22px;width:73px;height:198px">
    <p class="indicia-text" style="font-size:10px">********************ECRWSSEBBP****<br><br>Postal Customer<br>City, State, 5-Digit ZIP Code</p>
  </div>

  <p class="brand" style="left:262px;top:297px;font-size:19px">q7r Dental</p>
  <p class="abs" style="left:262px;top:338px;width:210px;font-size:7px;line-height:1.4;color:var(--ink)">Your Home for "Crown-to-Root Dental" Care!<br>Your local Geriatric, General &amp; Pediatric Dentistry.</p>
  <p class="abs" style="left:262px;top:366px;width:180px;font-size:7px;line-height:1.4;color:var(--ink)">New Patients and Emergency Dental Appointments are Welcome.</p>
  <p class="abs script" style="left:262px;top:405px;font-size:13px;color:var(--blue)">We are open<br>on Saturdays!</p>
  <p class="abs" style="left:262px;top:461px;font-size:9.5px;font-weight:700;line-height:1.4;color:var(--blue)">CALL US TOLL FREE!<br>1-800-q7r-DENT<br>(1-800-555-0142)</p>
  <div class="url-pill url-pill--blue" style="left:258px;top:517px;width:150px">www.q7rdental.com</div>

  <!-- Panel C -->
  <p class="brand" style="left:502px;top:46px;font-size:26px">q7r Dental</p>
  <p class="abs script" style="left:520px;top:104px;font-size:16px;color:var(--blue)">Your One-Stop</p>
  <p class="abs" style="left:501px;top:124px;font-size:19px;font-weight:700;color:var(--green)">Dental Destination.</p>
  <p class="abs script photo-caption" style="left:528px;top:451px;font-size:13.5px">So that you can smile</p>
  <p class="abs photo-caption" style="left:540px;top:467px;font-size:32px;font-weight:700;line-height:1">Forever</p>
  <p class="abs photo-caption" style="left:560px;top:497px;font-size:32px;font-weight:700;line-height:1">Together</p>
</section>

<section class="spread spread--inside" aria-label="Brochure inside">
  <svg class="spread-art" viewBox="0 0 720 556">
    <defs>
      <linearGradient id="familyPhoto" x1="0" y1="0" x2="1" y2="1">
        <stop offset="0" stop-color="#c9a58b"/><stop offset=".5" stop-color="#e3c3aa"/><stop offset="1" stop-color="#b58c76"/>
      </linearGradient>
      <linearGradient id="manPhoto" x1="0" y1="0" x2="0" y2="1">
        <stop offset="0" stop-color="#8fae6a"/><stop offset=".45" stop-color="#caa58a"/><stop offset="1" stop-color="#f2f2f0"/>
      </linearGradient>
      <linearGradient id="fatherSonPhoto" x1="0" y1="0" x2="1" y2="1">
        <stop offset="0" stop-color="#6b8a52"/><stop offset=".5" stop-color="#4b3a30"/><stop offset="1" stop-color="#2f6b3a"/>
      </linearGradient>
      <linearGradient id="deepBlue" x1="0" y1="0" x2="0" y2="1">
        <stop offset="0" stop-color="#1460a8"/><stop offset="1" stop-color="#0c4a8a"/>
      </linearGradient>
      <linearGradient id="paleBlue" x1="0" y1="0" x2="1" y2="0">
        <stop offset="0" stop-color="#ffffff"/><stop offset="1" stop-color="#eaf1f8"/>
      </linearGradient>
    </defs>
    <rect x="0" y="0" width="480" height="556" fill="url(#paleBlue)"/>
    <path role="img" aria-label="Photo of a happy family with parents and two young children" d="M0 0H240V190C200 205 150 225 0 222Z" fill="url(#familyPhoto)"/>
    <path d="M0 222C150 225 200 205 240 190V206C200 222 150 242 0 240Z" fill="#1460a8"/>
    <path d="M0 240C150 242 200 222 240 206V212C200 230 150 250 0 248Z" fill="#8dc63f"/>
    <path role="img" aria-label="Photo of a smiling young man outdoors" d="M240 362C300 330 400 318 480 322V556H240Z" fill="url(#manPhoto)"/>
    <path d="M240 362C300 330 400 318 480 322" stroke="#1460a8" stroke-width="7" fill="none"/>
    <path d="M240 354C300 322 400 310 480 314" stroke="#cddc39" stroke-width="4" fill="none"/>
    <path role="img" aria-label="Photo of a smiling father carrying his son on his back" d="M480 0H720V270C640 300 560 304 480 318Z" fill="url(#fatherSonPhoto)"/>
    <path d="M480 318C560 304 640 300 720 270V556H480Z" fill="url(#deepBlue)"/>
    <path d="M480 310C560 296 640 292 720 262V272C640 302 560 306 480 320Z" fill="#cddc39"/>
  </svg>

  <!-- Panel A -->
  <div class="photo-circle photo-circle--couple" role="img" aria-label="Photo of a smiling senior couple" style="left:70px;top:168px;width:84px;height:84px"></div>
  <div class="photo-circle photo-circle--smile" role="img" aria-label="Close-up photo of a bright smile" style="left:153px;top:180px;width:80px;height:80px"></div>
  <h2 class="abs head head--green" style="left:27px;top:256px;font-size:17px">Why</h2>
  <h2 class="abs head head--blue" style="left:27px;top:275px;font-size:17px">Implant Dentures?</h2>
  <ul class="ticks" style="left:29px;top:305px;width:205px;font-size:8.5px;color:var(--grey-text);line-height:1.3">
    <li style="height:22px"><svg width="14" height="14" viewBox="0 0 20 20"><path d="M2 9h4v9H2zM7 9l4-7c2 0 2 2 1.5 4H17c1.5 0 2 1 1.6 2.2l-2 7.5c-.3 1-1 1.3-2 1.3H7z" fill="#8dc63f"/></svg><span>Durable and Cost Effective</span></li>
    <li style="height:34px"><svg width="14" height="14" viewBox="0 0 20 20"><path d="M2 6c4 3 12 3 16 0v6c-4 4-12 4-16 0z" fill="#8dc63f"/></svg><span>Your denture fabricated as normal<br>denture</span></li>
    <li style="height:38px"><svg width="14" height="16" viewBox="0 0 20 22"><path d="M3 3c3-2 5 0 7 0s4-2 7 0c2 2 1 6-1 8h-12c-2-2-3-6-1-8z" fill="#8dc63f"/><path d="M7 13h6M7 16h6M8 19h4" stroke="#8dc63f" stroke-width="1.6"/></svg><span>Four or more implants are placed<br>in one visit</span></li>
    <li style="height:36px"><svg width="14" height="14" viewBox="0 0 20 20"><circle cx="10" cy="10" r="8" fill="none" stroke="#8dc63f" stroke-width="2"/><path d="M6 10l3 3 5-6" stroke="#8dc63f" stroke-width="2" fill="none"/></svg><span>Your denture is then retrofitted to<br>snap on the mini implant retention head</span></li>
    <li style="height:26px"><svg width="14" height="14" viewBox="0 0 20 20"><path d="M3 4c3-2 5 0 7 0s4-2 7 0c2 3 0 8-2 13-1 1-2 0-2-1l-1-4c-.5-1-1.5-1-2 0l-1 4c0 1-1 2-2 1C4 12 1 7 3 4z" fill="none" stroke="#8dc63f" stroke-width="1.6"/></svg><span>Stabilize your loose dentures in one visit</span></li>
  </ul>
  <p class="abs script" style="left:29px;top:490px;font-size:15.5px;color:var(--blue)">You deserve nothing less...</p>
  <p class="abs" style="left:25px;top:511px;font-size:25px;font-weight:700;color:var(--green)">A Beautiful Smile</p>

  <!-- Panel B -->
  <h2 class="abs head head--green" style="left:267px;top:34px;font-size:22px">Why</h2>
  <h2 class="abs head head--blue" style="left:267px;top:58px;font-size:22px">Mini Implants?</h2>
  <ul class="ticks" style="left:270px;top:98px;width:205px;font-size:11px;color:var(--grey-text);line-height:1.3">
    <li style="height:43px"><svg width="18" height="24" viewBox="0 0 20 22"><circle cx="6" cy="4" r="2.6" fill="none" stroke="#8dc63f" stroke-width="1.6"/><path d="M6 7v13" stroke="#8dc63f" stroke-width="2"/><path d="M14 2v18" stroke="#8dc63f" stroke-width="2"/><path d="M12 3h4" stroke="#8dc63f" stroke-width="2"/></svg><span>Less involved procedure than<br>conventional implants</span></li>
    <li style="height:44px"><svg width="18" height="18" viewBox="0 0 20 20"><rect x="2" y="4" width="16" height="14" rx="2" fill="none" stroke="#8dc63f" stroke-width="1.8"/><path d="M2 8h16M6 2v4M14 2v4" stroke="#8dc63f" stroke-width="1.8"/></svg><span>Usually completed in one<br>dental appointment</span></li>
    <li style="height:30px"><svg width="18" height="18" viewBox="0 0 20 20"><path d="M3 4c3-2 5 0 7 0s4-2 7 0c2 3 0 8-2 13-1 1-2 0-2-1l-1-4c-.5-1-1.5-1-2 0l-1 4c0 1-1 2-2 1C4 12 1 7 3 4z" fill="none" stroke="#8dc63f" stroke-width="1.6"/></svg><span>Replace missing teeth instantly</span></li>
  </ul>
  <p class="brand" style="left:274px;top:258px;font-size:25px">q7r Dental</p>

  <!-- Panel C -->
  <p class="abs script photo-caption" style="left:502px;top:200px;font-size:16px">Our Smiles</p>
  <p class="abs photo-caption" style="left:512px;top:220px;font-size:24px;font-weight:700;line-height:1">Speak For</p>
  <p class="abs photo-caption" style="left:542px;top:244px;font-size:24px;font-weight:700;line-height:1">Themselves</p>
  <div class="photo-circle photo-circle--smile" role="img" aria-label="Close-up photo of a bright smile" style="left:628px;top:264px;width:82px;height:82px;border-color:#cddc39"></div>
  <h2 class="abs head head--lime" style="left:503px;top:318px;font-size:18.5px">Implants <span style="font-size:10px">vs</span><br>Mini-Implants</h2>
  <p class="abs" style="left:503px;top:368px;width:196px;font-size:7.6px;line-height:1.42;color:#fff">Visit q7r Dental for a complementary consultation to learn which option is best for you. Depending on various conditions including that of the jawbone, you may be recommended an implant or mini-implant based treatment.</p>
  <p class="abs" style="left:503px;top:433px;width:196px;font-size:7.6px;line-height:1.42;color:#fff">Implant or Mini-implant treatment may not be suitable for all patients. For implants to be successful, you need to have healthy gums and adequate bones to support the implants. You must also be willing to commit to proper maintenance of your implants or dentures. Visit your dentist at q7r Dental to learn more.</p>
  <div class="url-pill url-pill--green" style="left:510px;top:524px;width:182px">www.q7rdental.com</div>
</section>

</body>
</html>
```